Rapidly growing regional logistics company looking for a modern clean website design.

We need a website for a 5 year old company based in New England.
We offer a complete logistics solution. With services dedicated to the changing economic environment. Services to our customers include, same day delivery, trucking and van service, warehouse & storage, pool distribution, and B2B installations.
We've implemented leading technology along the way, that provides visibility, accountability, up to the minute tracking, and project management.
Our goal to be known in the industry we service as an excellent provider of time-critical services and dependability.
Independently of the services we offer, our customers know that they can count on a true partner.

Target Market(s)

B2B, including printers, retail, manufacturers, wholesalers, electronics, any company that needs product delivered or warehoused

Industry/Entity Type

Logistics

Coding

Coded - Design and coding required

Number of Pages Required

5+ page

Font styles to use
Sans Serif

Colors
0255a3

Requirements
Must have
• Clean, modern design, limited clutter. Limited tabs, preferred everything on 1st screen roll down to see info

```html
<!DOCTYPE html>
<html lang="en">
<head>
<meta charset="utf-8">
<title>Northfield Logistics</title>
<link href="https://fonts.googleapis.com/css2?family=Open+Sans:wght@400;600;700&family=Roboto:wght@300;400;500;700&display=swap" rel="stylesheet">
<style>
:root{
  --brand:#0255a3;
  --brand-dark:#023f7a;
  --brand-mid:#1e63ad;
  --ink:#333c46;
  --muted:#6b7480;
  --paper:#ffffff;
  --mist:#eef1f4;
  --night:#2a2d31;
  --night-2:#1f2225;
}
*{box-sizing:border-box;margin:0;padding:0}
html,body{width:1200px;height:2964px;overflow:hidden}
body{font-family:"Open Sans",Arial,sans-serif;color:var(--ink);background:var(--paper);font-size:13px;line-height:1.6}
h1,h2,h3{font-family:"Roboto",Arial,sans-serif}
.btn{display:inline-block;background:var(--brand);color:#fff;font-size:12px;font-weight:600;padding:9px 24px;border-radius:2px;text-decoration:none;white-space:nowrap}
.btn--light{background:#fff;color:var(--brand)}

/* header + hero */
.hero{position:relative;height:472px;background:linear-gradient(100deg,#0a3d78 0%,#2a6fb4 45%,#6f9ccb 75%,#9ab6d3 100%);color:#fff}
.hero__photo{position:absolute;inset:0}
.nav{position:absolute;top:0;left:0;right:0;height:48px;background:rgba(10,25,45,.75);display:flex;align-items:center;padding:0 200px}
.brand{display:flex;align-items:center;gap:10px;font-family:"Roboto",sans-serif;font-weight:700;font-size:17px;color:#fff;letter-spacing:1px;margin-right:56px;white-space:nowrap}
.brand__dot{width:26px;height:26px;border-radius:50%;background:#fff;flex:none}
.nav__links{display:flex;gap:26px;list-style:none;font-size:12px;white-space:nowrap}
.nav__links a{color:#fff;text-decoration:none}
.hero__content{position:absolute;left:230px;top:74px;width:520px}
.hero__title{font-size:46px;font-weight:500;letter-spacing:1px;margin-bottom:14px}
.hero__text{font-size:14px;line-height:1.7;margin-bottom:22px}

/* service rows */
.service{position:relative;display:flex;align-items:center}
.service__media{position:absolute}
.service__body{position:absolute;width:520px}
.service__title{font-size:30px;font-weight:400;margin-bottom:4px}
.service__lead{font-weight:700;font-size:13px;margin-bottom:8px}
.service__body p{margin-bottom:10px;font-size:12px}
.service__list{list-style:none;font-size:12px;margin-bottom:16px}
.service__list li::before{content:"• "}
.service--white{background:var(--paper)}
.service--blue{background:var(--brand-mid);color:#fff}

.truck{height:428px}
.truck .service__media{left:90px;top:70px;width:400px;height:280px;background:linear-gradient(160deg,#f4f6f8,#d5dbe2);border-radius:4px}
.truck .service__body{left:540px;top:66px}

.pool{height:440px;overflow:hidden}
.pool .service__media{right:0;top:150px;width:520px;height:290px;background:linear-gradient(170deg,#3b79bd,#7a3a2e 70%,#b0573f)}
.pool .service__body{left:80px;top:28px;width:600px}
.pool__band{position:absolute;left:0;right:0;top:0;height:440px}

.sameday{height:420px}
.sameday .service__media{left:120px;top:70px;width:320px;height:290px;background:linear-gradient(160deg,#f6eee2,#d9b98b)}
.sameday .service__body{left:550px;top:56px;width:560px}

.dedicated{height:360px}
.dedicated .service__media{right:140px;top:24px;width:300px;height:320px;background:linear-gradient(160deg,#4c86c6,#c9a97c 60%,#a57d4d)}
.dedicated .service__body{left:160px;top:28px;width:600px}

/* about */
.about{height:440px;background:var(--paper);text-align:center;padding-top:40px}
.about__title{font-size:32px;font-weight:700;color:var(--brand);letter-spacing:1px}
.about__rule{width:60px;height:3px;background:var(--brand);margin:8px auto 22px}
.about p{width:880px;margin:0 auto 14px;font-size:12px;color:var(--muted)}

/* cta */
.cta{height:220px;background:var(--mist);text-align:center;padding-top:36px}
.cta__title{font-size:26px;font-weight:400;color:var(--ink)}
.cta__sub{font-size:11px;color:var(--muted);margin:4px 0 18px}
.cta__form{display:flex;justify-content:center;gap:14px}
.cta__field{width:150px;height:32px;background:#fff;border:1px solid #ccd3da;font-size:11px;color:#9aa3ad;padding:8px 10px;text-align:left}
.cta__form .btn{width:130px;padding:8px 0}

/* footer */
.footer{height:184px;background:var(--night);color:#c3c8ce;display:flex;padding:28px 120px 0;gap:60px}
.footer__col{width:210px;font-size:11px;line-height:1.7}
.footer__head{color:#fff;font-size:13px;font-weight:600;margin-bottom:8px}
.footer__col ul{list-style:none}
.footer__input{height:28px;background:#fff;width:180px;margin-bottom:8px;font-size:11px;color:#9aa3ad;padding:6px 8px}
.footer .btn{padding:6px 24px;font-size:11px}
</style>
</head>
<body>

<header class="hero">
  <div class="hero__photo" role="img" aria-label="Warehouse interior with a worker in a hard hat and safety vest, blue tinted"></div>
  <nav class="nav">
    <div class="brand"><span class="brand__dot"></span>NORTHFIELD</div>
    <ul class="nav__links">
      <li><a href="#">Home</a></li>
      <li><a href="#">Warehousing</a></li>
      <li><a href="#">Truck &amp; Van Service</a></li>
      <li><a href="#">Distribution &amp; Pool Service</a></li>
      <li><a href="#">Contact</a></li>
      <li><a href="#">About Us</a></li>
    </ul>
  </nav>
  <div class="hero__content">
    <h1 class="hero__title">WAREHOUSING</h1>
    <p class="hero__text">Our warehouse facility may prove to be one of the most valuable extensions of your company's operations. With a secure warehouse conveniently located in central New England to supplement your firm's storage and distribution needs.</p>
    <a class="btn" href="#">Contact Us</a>
  </div>
</header>

<section class="service service--white truck">
  <div class="service__media" role="img" aria-label="White box truck with company branding"></div>
  <div class="service__body">
    <h2 class="service__title">Truck &amp; Van Service</h2>
    <p class="service__lead">Trucking, vehicle and ground transportation include:</p>
    <ul class="service__list">
      <li>Dock to dock scheduled delivery</li>
      <li>Light and heavy trucking across New England</li>
      <li>Lift gate and pallet jack equipped vehicles</li>
      <li>Time-critical and dedicated runs on demand</li>
      <li>Live tracking and proof of delivery</li>
      <li>Vans and box trucks available day and night</li>
    </ul>
    <p>Whatever you ship, trust us to handle shipments with care and on time.</p>
    <a class="btn" href="#">Contact Us</a>
  </div>
</section>

<section class="service service--blue pool">
  <svg class="pool__band" width="1200" height="440" viewBox="0 0 1200 440" aria-hidden="true">
    <polygon points="0,0 1200,0 1200,150 640,440 0,440" fill="#0255a3"/>
  </svg>
  <div class="service__media" role="img" aria-label="Container ship loaded with cargo at sea"></div>
  <div class="service__body">
    <h2 class="service__title">Distribution &amp; Pool Service</h2>
    <p>Pool distribution consolidates many smaller shipments into one load bound for a single geographic region. Freight moves together to a local terminal and is then broken down and delivered to each final stop, saving cost, handling and transit time for our customers.</p>
    <p>Our distribution team plans each route with up to the minute tracking, so every shipment is visible and accounted for from pickup to delivery.</p>
    <p>Whether you ship to retail stores, printers or wholesalers, we build a program around your schedule and volume.</p>
    <a class="btn btn--light" href="#">Contact Us</a>
  </div>
</section>

<section class="service service--white sameday">
  <div class="service__media" role="img" aria-label="Stacked cardboard shipping boxes"></div>
  <div class="service__body">
    <h2 class="service__title">Same-day Delivery Service</h2>
    <p>Regardless of the size of your order, our same-day team is ready to pick up and deliver the very same day. We move documents, parts and pallets across the region with speed and care, keeping you informed at every step.</p>
    <p>Our dispatchers track each delivery in real time, giving you full visibility and a proof of delivery the moment your goods arrive. Time-critical work is what we do best.</p>
    <a class="btn" href="#">Contact Us</a>
  </div>
</section>

<section class="service service--blue dedicated">
  <div class="service__media" role="img" aria-label="Boxes stacked on a hand truck"></div>
  <div class="service__body">
    <h2 class="service__title">Dedicated Delivery Service</h2>
    <p>A dedicated fleet gives you drivers and vehicles that work only for your company, on your schedule and to your standards. Whether you need a van or a full truck, we can provide the solution for you.</p>
    <p>Our drivers learn your routes, your customers and your products, delivering consistent service day after day while our technology keeps every run accountable.</p>
    <a class="btn btn--light" href="#">Contact Us</a>
  </div>
</section>

<section class="about">
  <h2 class="about__title">ABOUT US</h2>
  <div class="about__rule"></div>
  <p>Our company was founded in 2013 and has been in business with a combined 75 years of experience.</p>
  <p>Northfield Logistics offers a complete logistics solution, with services dedicated to the changing economic environment. Services to our customers include same day delivery, trucking and van service, warehouse &amp; storage, pool distribution, and B2B installations.</p>
  <p>We've implemented leading technology along the way, that provides visibility, accountability, up to the minute tracking, and project management.</p>
  <p>Our goal is to be known in the industry we service as an excellent provider of time-critical services and dependability.</p>
  <p>Independently of the services we offer, our customers know that they can count on a true partner.</p>
</section>

<section class="cta">
  <h2 class="cta__title">Would you like to see more?</h2>
  <p class="cta__sub">Send us a short note and a team member will reach out to you within one business day.</p>
  <div class="cta__form">
    <div class="cta__field">Name</div>
    <div class="cta__field">Email Address</div>
    <div class="cta__field">Phone Number</div>
    <div class="cta__field">Company</div>
    <a class="btn" href="#">Send</a>
  </div>
</section>

<footer class="footer">
  <div class="footer__col">
    <div class="footer__head">About Us</div>
    <p>Northfield Logistics is a regional carrier serving New England with same day, trucking, pool and warehouse services.</p>
  </div>
  <div class="footer__col">
    <div class="footer__head">Social</div>
    <ul><li>Company news</li><li>Service updates</li><li>Driver careers</li></ul>
  </div>
  <div class="footer__col">
    <div class="footer__head">Contact Us</div>
    <ul><li>48 Orchard Lane, Unit 2</li><li>Millbrook, MA 01000</li><li>Phone: (555) 014-2290</li><li>Email: info@northfield.example</li></ul>
  </div>
  <div class="footer__col">
    <div class="footer__head">Get Started</div>
    <div class="footer__input">Email Address</div>
    <a class="btn" href="#">Subscribe</a>
  </div>
</footer>

</body>
</html>
```